Postcard Mailer

We are a pizza pub that is the only local restaurant that offers and delivers pizza, burgers, salads and wings.

We just opened and want to send out a postcard to the community. thinking on one side a nice design with pics etc. then on the back a list of our daily food and drink specials.

Restaurant

eb1f27

```html
<!DOCTYPE html>
<html lang="en">
<head>
<meta charset="utf-8">
<title>Rosa and Marco – Postcard Mailer</title>
<link href="https://fonts.googleapis.com/css2?family=Open+Sans:ital,wght@0,400;0,600;0,700;1,700&family=Oswald:wght@400;500&family=Roboto+Condensed:wght@700&family=Berkshire+Swash&family=Patrick+Hand&display=swap" rel="stylesheet">
<style>
  :root{
    --bg:#e4e5e8;
    --brand:#eb1f27;
    --maroon-dark:#5e0a0e;
    --maroon:#8c1117;
    --maroon-mid:#b3161e;
    --gold:#d9a93a;
    --white:#ffffff;
    --ink:#1a1a1a;
    --line:#c9848a;
  }
  *{box-sizing:border-box;margin:0;padding:0}
  html,body{width:1200px;height:900px;overflow:hidden}
  body{background:var(--bg);font-family:'Open Sans',sans-serif;position:relative}

  .card{position:absolute;top:256px;width:570px;height:388px;overflow:hidden;box-shadow:0 6px 18px rgba(0,0,0,.25)}
  .card--front{left:20px;background:radial-gradient(ellipse at 55% 35%,var(--maroon-mid) 0%,var(--maroon) 45%,var(--maroon-dark) 100%)}
  .card--back{left:610px;background:var(--white)}

  /* front */
  .brand{position:absolute;left:20px;top:32px;width:110px;text-align:center;color:var(--white)}
  .brand__mark{width:56px;height:56px;border-radius:50%;background:var(--white);margin:0 auto 6px}
  .brand__name{font-weight:700;font-size:10px;letter-spacing:.5px;text-transform:uppercase}
  .brand__town{font-weight:700;font-size:6px;margin-top:3px}
  .brand__phone{font-weight:700;font-size:12px;margin-top:2px}

  .topping-banner{position:absolute;left:145px;top:38px;width:282px;height:48px;border-radius:3px;
    background:linear-gradient(180deg,#e8333a,#a3121a);border:2px solid #f05b60;box-shadow:0 2px 5px rgba(0,0,0,.5);
    color:var(--white);font-family:'Oswald',sans-serif;text-align:center;padding-top:5px}
  .topping-banner__title{font-size:13px;letter-spacing:.2px}
  .topping-banner__prices{font-size:9.5px;word-spacing:2px}
  .topping-banner__prices span{margin:0 18px}

  .deliver-badge{position:absolute;left:438px;top:10px;width:94px;height:94px}
  .deliver-badge__text{position:absolute;inset:0;display:flex;flex-direction:column;align-items:center;justify-content:center;color:var(--white);line-height:1.05}
  .deliver-badge__we{font-weight:700;font-size:14px}
  .deliver-badge__deliver{font-weight:600;font-size:10px}
  .deliver-badge__online{font-size:8px}

  .swoosh{position:absolute;left:0;top:0}

  .pill{position:absolute;color:var(--white);font-family:'Oswald',sans-serif;font-size:14px;border-radius:12px;
    background:linear-gradient(180deg,#f0333a,#b5151d);box-shadow:0 2px 4px rgba(0,0,0,.45);padding:1px 12px;white-space:nowrap}
  .pill--pizza{left:334px;top:94px}
  .pill--specialty{left:160px;top:136px}
  .pill--calzones{left:425px;top:120px}

  .photo{position:absolute}
  .photo--pizza{left:36px;top:172px;width:270px;height:146px;border-radius:50%;background:radial-gradient(ellipse,#b0492e 0%,#c98b4e 75%,#9a9da2 100%)}
  .photo--salad{left:228px;top:138px;width:190px;height:162px;border-radius:50%;background:radial-gradient(ellipse,#8a7f50 0%,#3f6a2a 65%,#1e1e1e 100%)}
  .photo--burger{left:408px;top:165px;width:146px;height:118px;border-radius:40% 40% 18% 18%;background:radial-gradient(ellipse at 50% 40%,#e0a75a 0%,#c27f3e 70%,#9a5a2c 100%)}

  .reverse-note{position:absolute;left:340px;top:320px;background:var(--white);color:var(--ink);
    font-family:'Patrick Hand',cursive;font-size:14px;padding:0 12px;border-radius:10px}
  .tagline{position:absolute;left:58px;top:348px;color:var(--white);line-height:1.1}
  .tagline__lead{font-family:'Berkshire Swash',cursive;font-size:17px}
  .tagline__sub{font-family:'Open Sans',sans-serif;font-style:italic;font-weight:700;font-size:15px}

  /* back */
  .menu-panel{position:absolute;left:0;top:0;width:286px;height:100%;background:linear-gradient(180deg,var(--maroon-mid),var(--maroon) 60%,var(--maroon-dark))}
  .specials{position:absolute;left:20px;top:44px;width:150px;color:var(--white)}
  .specials__day{margin-bottom:9px}
  .specials__name{font-weight:700;font-style:italic;font-size:8.5px}
  .specials__item{font-size:7.5px;line-height:1.25}
  .price-list{position:absolute;left:168px;top:14px;width:108px;display:flex;flex-direction:column;gap:12px}
  .price-tag{background:var(--white);border:3px solid var(--gold);outline:2px dashed var(--brand);outline-offset:-6px;border-radius:12px;
    font-family:'Roboto Condensed',sans-serif;font-weight:700;font-size:12px;color:var(--ink);text-align:center;line-height:1.15;
    height:72px;display:flex;align-items:center;justify-content:center}
  .stamp-box{position:absolute;right:18px;top:14px;width:62px;height:80px;border:1.5px solid var(--maroon-mid)}
  .address-lines{position:absolute;left:306px;top:198px;width:246px}
  .address-lines span{display:block;border-top:1px solid var(--line);height:25px}
</style>
</head>
<body>

<section class="card card--front" aria-label="Postcard front">
  <svg class="swoosh" width="570" height="388" viewBox="0 0 570 388" aria-hidden="true">
    <path d="M0 176 C120 150 300 112 570 92" fill="none" stroke="var(--gold)" stroke-width="1.5"/>
    <path d="M28 338 C200 325 400 308 560 292" fill="none" stroke="var(--gold)" stroke-width="2"/>
  </svg>

  <div class="brand">
    <div class="brand__mark"></div>
    <div class="brand__name">Rosa and Marco</div>
    <div class="brand__town">HARBOR TOWN, NC</div>
    <div class="brand__phone">910 555 0148</div>
  </div>

  <div class="topping-banner">
    <div class="topping-banner__title">BUILD YOUR OWN CHOOSE YOUR TOPPINGS</div>
    <div class="topping-banner__prices"><span>MEDIUM +$1.50</span><span>LARGE +$2.25</span></div>
  </div>

  <div class="deliver-badge">
    <svg width="94" height="94" viewBox="0 0 94 94" aria-hidden="true">
      <polygon fill="var(--white)" points="47,2 54,10 64,5 68,15 79,14 79,25 89,29 85,39 92,47 85,55 89,65 79,69 79,80 68,79 64,89 54,84 47,92 40,84 30,89 26,79 15,80 15,69 5,65 9,55 2,47 9,39 5,29 15,25 15,14 26,15 30,5 40,10"/>
      <circle cx="47" cy="47" r="35" fill="var(--maroon)"/>
    </svg>
    <div class="deliver-badge__text">
      <span class="deliver-badge__we">WE</span>
      <span class="deliver-badge__deliver">Deliver</span>
      <span class="deliver-badge__online">Order on-line</span>
    </div>
  </div>

  <div class="photo photo--salad" role="img" aria-label="Photo of a salad with greens, tomato, cheese, cranberries and pear with dressing"></div>
  <div class="photo photo--pizza" role="img" aria-label="Photo of a pepperoni and sausage pizza on a metal tray"></div>
  <div class="photo photo--burger" role="img" aria-label="Photo of a double cheeseburger with lettuce and tomato"></div>

  <span class="pill pill--pizza">PIZZA</span>
  <span class="pill pill--specialty">SPECIALTY PIZZAS</span>
  <span class="pill pill--calzones">CALZONES</span>

  <div class="reverse-note">see reverse for our menu</div>

  <div class="tagline">
    <div class="tagline__lead">Taste The Difference</div>
    <div class="tagline__sub">Fresh Ingredients Make!</div>
  </div>
</section>

<section class="card card--back" aria-label="Postcard back">
  <div class="menu-panel">
    <div class="specials">
      <div class="specials__day"><div class="specials__name">Tuesday</div><div class="specials__item">Medium Pizza $7.95<br>50 cent wings<br>$1.50 Drafts</div></div>
      <div class="specials__day"><div class="specials__name">Wednesday</div><div class="specials__item">Classic Burger + Beer $5.95<br>$2.50 Cinnamon Shots</div></div>
      <div class="specials__day"><div class="specials__name">Thursday</div><div class="specials__item">$1 Slice Night<br>$2.50 Craft Beers</div></div>
      <div class="specials__day"><div class="specials__name">Friday</div><div class="specials__item">2 Medium Pizzas $15.95<br>$2 Glasses of Wine</div></div>
      <div class="specials__day"><div class="specials__name">Saturday</div><div class="specials__item">1/2 Price Salads<br>$3 Vodka Drinks<br>$2.50 House IPA</div></div>
      <div class="specials__day"><div class="specials__name">Sunday</div><div class="specials__item">Large Pizza $9.95<br>$3 Bloody Mary's &amp; Mimosa's</div></div>
    </div>
    <div class="price-list">
      <div class="price-tag">Medium 14”<br>Pie $11.95</div>
      <div class="price-tag">Large 16”<br>Pie $13.95</div>
      <div class="price-tag">Speciality Pizzas<br>Medium 14”<br>$13.95</div>
      <div class="price-tag">Speciality Pizzas<br>Large 16”<br>$18.95</div>
    </div>
  </div>
  <div class="stamp-box" aria-label="Stamp area"></div>
  <div class="address-lines" aria-label="Address lines"><span></span><span></span><span></span><span></span><span></span></div>
</section>

</body>
</html>
```